Harborview Wellness Counseling
7 business cards, letterhead, envlp, fax cover
Harborview Wellness Counseling -
Creative Brief
Professional
Martin Oakridge
Owner/Manager
2875 Pellham Ridge Blvd. Suite 204 Lakemont, MO 63412
oakridgehome@brisknet-mail.net
I need cards for each of my seven therapists. I will upload word file with their names and info. Letterhead should not use therapists names.

```html
<!DOCTYPE html>
<html lang="en">
<head>
<meta charset="utf-8">
<title>Harborview Wellness Counseling – Stationery</title>
<link href="https://fonts.googleapis.com/css2?family=Open+Sans:wght@400;600;700&display=swap" rel="stylesheet">
<style>
:root{
  --navy:#1f3a6e;
  --orange:#e87722;
  --yellow:#f6c21b;
  --green:#7ab648;
  --blue:#2a8bc9;
  --ink:#555b63;
  --paper:#ffffff;
  --bg:#e9e7e3;
  --rule:#d5d8dc;
  --cell:#f2f3f5;
  --halo:#efe9df;
}
*{box-sizing:border-box;margin:0;padding:0}
html,body{width:1200px;height:891px;overflow:hidden;background:var(--bg);font-family:"Open Sans",Arial,sans-serif;color:var(--ink)}
.canvas{position:relative;width:1200px;height:891px}
.sheet{position:absolute;background:var(--paper);box-shadow:0 2px 6px rgba(0,0,0,.18);overflow:hidden}
.stripe{position:absolute;left:0;top:0;width:6px;display:flex;flex-direction:column}
.stripe i{flex:1}
.stripe i:nth-child(1){background:var(--orange)}
.stripe i:nth-child(2){background:var(--yellow)}
.stripe i:nth-child(3){background:var(--green)}
.stripe i:nth-child(4){background:var(--blue)}
.brand{position:absolute;display:flex;align-items:center;gap:6px;color:var(--navy);font-weight:700;text-transform:uppercase;white-space:nowrap}
.brand .dot{border-radius:50%;background:var(--orange);flex:none}

/* business cards */
.card{width:312px;height:132px}
.card .stripe{height:58px}
.card .brand{left:16px;top:12px;font-size:10.5px}
.card .brand .dot{width:14px;height:14px}
.card .person{position:absolute;left:18px;top:40px}
.card .name{font-size:9px;font-weight:700;color:var(--orange)}
.card .title{font-size:7px}
.card .contact{position:absolute;left:18px;top:78px;font-size:6.5px;line-height:1.45}
.card .badge{position:absolute;right:18px;bottom:18px;width:70px;height:70px;border-radius:50%;border:2px solid #eef1f4}

/* letterhead & fax */
.page{width:298px;height:423px;top:446px}
.page .stripe{height:120px;width:7px}
.page .brand{left:18px;top:22px;font-size:12px}
.page .brand .dot{width:18px;height:18px}
.page .watermark{position:absolute;left:50%;top:200px;width:150px;height:150px;margin-left:-75px;border-radius:50%;border:3px solid var(--halo)}
.page .footer{position:absolute;left:0;right:0;bottom:16px;text-align:center;font-size:5.5px;line-height:1.5}
.fax-word{position:absolute;right:22px;top:74px;font-size:16px;font-weight:700;color:var(--navy)}
.fax-table{position:absolute;left:18px;top:96px;width:262px;border-collapse:collapse;font-size:6.5px;table-layout:fixed}
.fax-table td{border-bottom:1px solid var(--rule);height:13px;padding-left:3px;background:var(--cell)}
.fax-table td.label{width:16%;color:var(--navy);font-weight:600}
.checks{position:absolute;left:18px;width:262px;top:164px;display:flex;justify-content:space-between;font-size:5px;white-space:nowrap}
.checks span::before{content:"";display:inline-block;width:5px;height:5px;border:1px solid var(--ink);margin-right:2px;vertical-align:-1px}
.fax-line{position:absolute;left:18px;width:40px;top:180px;border-top:1px solid var(--ink)}

/* envelope */
.envelope{left:730px;top:446px;width:333px;height:300px;background:none;box-shadow:none;overflow:visible}
.env-front{position:absolute;left:0;top:0;width:333px;height:150px;background:var(--paper);box-shadow:0 2px 6px rgba(0,0,0,.18)}
.env-front .stripe{height:60px}
.env-front .brand{left:16px;top:16px;font-size:10.5px}
.env-front .brand .dot{width:14px;height:14px}
.env-front .return{position:absolute;left:16px;bottom:12px;font-size:5.5px;white-space:nowrap}
.env-front .badge{position:absolute;left:150px;top:30px;width:80px;height:80px;border-radius:50%;border:2px solid #eef1f4}
.env-back{position:absolute;left:0;top:160px;width:333px;height:140px;box-shadow:0 2px 6px rgba(0,0,0,.18)}
</style>
</head>
<body>
<main class="canvas">

  <section class="sheet card" style="left:127px;top:29px"><div class="stripe"><i></i><i></i><i></i><i></i></div><div class="badge"></div><div class="brand"><span class="dot"></span>Harborview Wellness Counseling</div><div class="person"><p class="name">Martin Oakridge, Ph.D.</p><p class="title">Licensed Psychologist</p></div><div class="contact"><p>2875 Pellham Ridge Blvd. Suite 204</p><p>Lakemont, MO 63412</p><p>Phone (555) 014-2200 &nbsp;|&nbsp; Fax (555) 014-2201</p><p>oakridgehome@brisknet-mail.net</p></div></section>
  <section class="sheet card" style="left:470px;top:29px"><div class="stripe"><i></i><i></i><i></i><i></i></div><div class="badge"></div><div class="brand"><span class="dot"></span>Harborview Wellness Counseling</div><div class="person"><p class="name">Lisa Hartwell, LPC</p><p class="title">Licensed Counselor</p></div><div class="contact"><p>2875 Pellham Ridge Blvd. Suite 204</p><p>Lakemont, MO 63412</p><p>Phone (555) 014-2200 &nbsp;|&nbsp; Fax (555) 014-2201</p><p>oakridgehome@brisknet-mail.net</p></div></section>
  <section class="sheet card" style="left:857px;top:29px"><div class="stripe"><i></i><i></i><i></i><i></i></div><div class="badge"></div><div class="brand"><span class="dot"></span>Harborview Wellness Counseling</div><div class="person"><p class="name">Ruth Kramer</p><p class="title">Office Manager</p></div><div class="contact"><p>2875 Pellham Ridge Blvd. Suite 204</p><p>Lakemont, MO 63412</p><p>Phone (555) 014-2200 &nbsp;|&nbsp; Fax (555) 014-2201</p><p>oakridgehome@brisknet-mail.net</p></div></section>

  <section class="sheet card" style="left:127px;top:173px"><div class="stripe"><i></i><i></i><i></i><i></i></div><div class="badge"></div><div class="brand"><span class="dot"></span>Harborview Wellness Counseling</div><div class="person"><p class="name">Janet Boyd, Ph.D.</p><p class="title">Licensed Psychologist</p></div><div class="contact"><p>2875 Pellham Ridge Blvd. Suite 204</p><p>Lakemont, MO 63412</p><p>Phone (555) 014-2200 &nbsp;|&nbsp; Fax (555) 014-2201</p><p>oakridgehome@brisknet-mail.net</p></div></section>
  <section class="sheet card" style="left:470px;top:173px"><div class="stripe"><i></i><i></i><i></i><i></i></div><div class="badge"></div><div class="brand"><span class="dot"></span>Harborview Wellness Counseling</div><div class="person"><p class="name">Carla Voss, Ph.D.</p><p class="title">Licensed Psychologist</p></div><div class="contact"><p>2875 Pellham Ridge Blvd. Suite 204</p><p>Lakemont, MO 63412</p><p>Phone (555) 014-2200 &nbsp;|&nbsp; Fax (555) 014-2201</p><p>oakridgehome@brisknet-mail.net</p></div></section>
  <section class="sheet card" style="left:857px;top:173px"><div class="stripe"><i></i><i></i><i></i><i></i></div><div class="badge"></div><div class="brand"><span class="dot"></span>Harborview Wellness Counseling</div><div class="person"><p class="name">Paul Mercer, Ph.D.</p><p class="title">Licensed Psychologist</p></div><div class="contact"><p>2875 Pellham Ridge Blvd. Suite 204</p><p>Lakemont, MO 63412</p><p>Phone (555) 014-2200 &nbsp;|&nbsp; Fax (555) 014-2201</p><p>oakridgehome@brisknet-mail.net</p></div></section>

  <section class="sheet card" style="left:127px;top:317px"><div class="stripe"><i></i><i></i><i></i><i></i></div><div class="badge"></div><div class="brand"><span class="dot"></span>Harborview Wellness Counseling</div><div class="person"><p class="name">Amy Linden, Psy.D.</p><p class="title">Licensed Psychologist</p></div><div class="contact"><p>2875 Pellham Ridge Blvd. Suite 204</p><p>Lakemont, MO 63412</p><p>Phone (555) 014-2200 &nbsp;|&nbsp; Fax (555) 014-2201</p><p>oakridgehome@brisknet-mail.net</p></div></section>
  <section class="sheet card" style="left:470px;top:317px"><div class="stripe"><i></i><i></i><i></i><i></i></div><div class="badge"></div><div class="brand"><span class="dot"></span>Harborview Wellness Counseling</div><div class="person"><p class="name">Grace Holt, Ph.D.</p><p class="title">Licensed Psychologist</p></div><div class="contact"><p>2875 Pellham Ridge Blvd. Suite 204</p><p>Lakemont, MO 63412</p><p>Phone (555) 014-2200 &nbsp;|&nbsp; Fax (555) 014-2201</p><p>oakridgehome@brisknet-mail.net</p></div></section>
  <section class="sheet card" style="left:857px;top:317px"><div class="stripe"><i></i><i></i><i></i><i></i></div><div class="badge"></div><div class="brand"><span class="dot"></span>Harborview Wellness Counseling</div><div class="person"><p class="name">Ellen Marsh, LCSW</p><p class="title">Clinical Social Worker</p></div><div class="contact"><p>2875 Pellham Ridge Blvd. Suite 204</p><p>Lakemont, MO 63412</p><p>Phone (555) 014-2200 &nbsp;|&nbsp; Fax (555) 014-2201</p><p>oakridgehome@brisknet-mail.net</p></div></section>

  <section class="sheet page letterhead" style="left:115px">
    <div class="stripe"><i></i><i></i><i></i><i></i></div>
    <div class="brand"><span class="dot"></span>Harborview Wellness Counseling</div>
    <div class="watermark"></div>
    <div class="footer"><p>2875 Pellham Ridge Blvd. Suite 204 &nbsp;Lakemont, MO 63412</p><p>Phone (555) 014-2200 &nbsp;|&nbsp; Fax (555) 014-2201 &nbsp;|&nbsp; oakridgehome@brisknet-mail.net</p></div>
  </section>

  <section class="sheet page fax-cover" style="left:425px">
    <div class="stripe"><i></i><i></i><i></i><i></i></div>
    <div class="brand"><span class="dot"></span>Harborview Wellness Counseling</div>
    <p class="fax-word">FAX</p>
    <table class="fax-table">
      <tr><td class="label">To</td><td></td><td class="label">From</td><td></td></tr>
      <tr><td class="label">Phone</td><td></td><td class="label">Fax</td><td></td></tr>
      <tr><td class="label">Pages</td><td></td><td class="label">Date</td><td></td></tr>
      <tr><td class="label">Re</td><td></td><td class="label">CC</td><td></td></tr>
    </table>
    <div class="checks"><span>Urgent</span><span>For Review</span><span>Please Comment</span><span>Please Reply</span><span>Please Recycle</span></div>
    <div class="fax-line"></div>
    <div class="watermark" style="top:230px"></div>
    <div class="footer"><p>2875 Pellham Ridge Blvd. Suite 204 &nbsp;Lakemont, MO 63412</p><p>Phone (555) 014-2200 &nbsp;|&nbsp; Fax (555) 014-2201 &nbsp;|&nbsp; oakridgehome@brisknet-mail.net</p></div>
  </section>

  <section class="sheet envelope">
    <div class="env-front">
      <div class="stripe"><i></i><i></i><i></i><i></i></div>
      <div class="brand"><span class="dot"></span>Harborview Wellness Counseling</div>
      <div class="badge"></div>
      <p class="return">2875 Pellham Ridge Blvd. Suite 204 &nbsp;Lakemont, MO 63412 &nbsp;|&nbsp; oakridgehome@brisknet-mail.net</p>
    </div>
    <svg class="env-back" viewBox="0 0 333 140" aria-hidden="true">
      <rect x="0" y="0" width="333" height="140" fill="#ffffff"/>
      <polygon points="0,0 333,0 333,10 166.5,62 0,10" fill="#1f3a6e"/>
      <polyline points="0,140 150,70 183,70 333,140" fill="none" stroke="#e2e4e7" stroke-width="1"/>
      <circle cx="166.5" cy="40" r="8" fill="#e87722"/>
    </svg>
  </section>

</main>
</body>
</html>
```